Business Card Design Project

Attached is a rough business card design. We like this general design but we feel that the layout, text, color can use improvement and we seek the help of a professional designer.
We have a television and film production company based in New York. We need our cards for television network executives, other production executives, financiers etc. We deal with creative types as well as business people so we need the card to be interesting and edgy just like the name of our company - KICKTHEDOOR. The design should reflect the edgy, punk rock attitude of our company.
We prefer orange typeface for the logo but we're open to other ideas. I am attaching our existing business card and other files to help with the design.
Thank you in advance!!
Updates
Target Market(s)
Television and film producers, television network executives, other production executives, financiers, distribution companies
Industry/Entity Type
Film Production
Requirements
Must have
- I am attaching a photo of the company mascot which is a dog. We prefer to have the dog's photo as part of the card but we're open to the other ideas.
Name, phone number, email

```html
<!DOCTYPE html>
<html lang="en">
<head>
<meta charset="utf-8">
<title>Kick The Door – Business Card</title>
<link rel="stylesheet" href="https://fonts.googleapis.com/css2?family=Open+Sans:ital,wght@0,600;0,700;1,400&display=swap">
<style>
  :root {
    --brand-orange: #ec6526;
    --ink-black: #0c0c0c;
    --paper-white: #ffffff;
    --photo-warm: #c9a285;
    --photo-light: #efe4da;
    --photo-shadow: #8a6b55;
  }
  html, body {
    margin: 0;
    padding: 0;
    width: 1200px;
    height: 720px;
    overflow: hidden;
    background: var(--paper-white);
  }
  .business-card {
    position: relative;
    width: 1200px;
    height: 720px;
    background: var(--brand-orange);
    font-family: "Open Sans", Arial, sans-serif;
    color: var(--ink-black);
  }
  .card-artwork {
    position: absolute;
    inset: 0;
    width: 1200px;
    height: 720px;
  }
  .company-name {
    position: absolute;
    left: 630px;
    top: 152px;
    width: 560px;
    margin: 0;
    text-align: center;
    font-family: "Open Sans", Arial, sans-serif;
    font-weight: 700;
    font-size: 54px;
    letter-spacing: 3px;
    color: var(--brand-orange);
    line-height: 1;
  }
  .person-name {
    position: absolute;
    left: 630px;
    top: 248px;
    width: 560px;
    margin: 0;
    text-align: center;
    font-weight: 600;
    font-size: 96px;
    letter-spacing: -1px;
    line-height: 1;
  }
  .contact-list {
    position: absolute;
    left: 663px;
    top: 385px;
    margin: 0;
    padding: 0;
    list-style: none;
    font-size: 37px;
    line-height: 62px;
  }
  .contact-label {
    font-weight: 700;
  }
  .contact-value {
    font-style: italic;
    font-weight: 400;
  }
</style>
</head>
<body>
  <main class="business-card">
    <svg class="card-artwork" viewBox="0 0 1200 720" xmlns="http://www.w3.org/2000/svg">
      <defs>
        <clipPath id="band-clip">
          <path d="M0,195 C350,172 700,88 1200,62 L1200,498 C800,512 400,588 0,602 Z"/>
        </clipPath>
        <linearGradient id="photo-tones" x1="0" y1="0" x2="1" y2="1">
          <stop offset="0" stop-color="var(--photo-light)"/>
          <stop offset="0.45" stop-color="var(--photo-warm)"/>
          <stop offset="1" stop-color="var(--photo-shadow)"/>
        </linearGradient>
        <linearGradient id="photo-fade" x1="0" y1="0" x2="1" y2="0">
          <stop offset="0" stop-color="#ffffff" stop-opacity="0"/>
          <stop offset="0.55" stop-color="#ffffff" stop-opacity="0"/>
          <stop offset="1" stop-color="#ffffff" stop-opacity="1"/>
        </linearGradient>
      </defs>

      <path class="swoosh" fill="var(--ink-black)"
            d="M0,150 C400,120 700,55 1200,12 L1200,528 C800,560 400,650 0,662 Z"/>

      <path class="white-band" fill="var(--paper-white)"
            d="M0,195 C350,172 700,88 1200,62 L1200,498 C800,512 400,588 0,602 Z"/>

      <g clip-path="url(#band-clip)">
        <rect class="mascot-photo" role="img"
              aria-label="Photo of the company mascot, a French bulldog lying down with a small soccer ball"
              x="0" y="60" width="660" height="560" fill="url(#photo-tones)"/>
        <rect x="0" y="60" width="662" height="560" fill="url(#photo-fade)"/>
      </g>
    </svg>

    <h1 class="company-name">KICK THE DOOR</h1>
    <p class="person-name">John Doe</p>
    <ul class="contact-list">
      <li><span class="contact-label">Phone:</span> <span class="contact-value">(917) 555-0148</span></li>
      <li><span class="contact-label">E-Mail:</span> <span class="contact-value">info@kickthedoor.com</span></li>
    </ul>
  </main>
</body>
</html>
```